Podcast Art for Tidy Belly Talks: Rising above Bramwell's Ache

Read carefully Please. Most submittals so far have not read this.

We're looking for stunning, eye-catching, innovative yet simple podcast art for our first Podcast

Background should be solid, one color

Tidy Belly Talks: Rising with Bramwell's Ache
with Marcus Lindqvar

Use our Brand Guide including logo, colors, and font
https://lnk.example-short.net/TBT2020StyleBook

Some Podcast Covers I like: https://casts.wavelotte.net/

Optional: Mighty Flusher graphic included above and/or my headshot uploaded below

As you can see humor / medutainment is part of the brand. As we are talking serious topic such as a disease many suffer from you can see the humor in the logo and "mighty flusher" . Here is the monologue for the first episode to give you a deeper feel on the content

https://files.papernook.net/doc/7qR_Lm3vTz9KpWx2eHdN4bYcA51FgUoJsMiXwQeVZ/view?share=1

Target Market(s)

Those who suffer from gut issues, are diagnosed with inflammatory bowel disease(IBD), Crohn's Disease or Ulcerative Colitis - also their coaches, doctors, practitioners so functional or integrative medicine doctors/coaches, gastroenterologists etc.

Industry/Entity Type

Health And Wellness

Font styles to use
Other font styles liked:
• Primary: Oswald bold. Secondary: Oswald Medium or light

Requirements
Must have
• 3000 x 3000 pixels
Simple and eye-catching
Brand Guide Logo
Brand Guide Font
Brand Guide Colors including accent color(s)
I did not select colors below because I have included our Brand guide. Please use the exact colors there.
Nice to have
• Maybe my headshot and/or the mighty flusher graphic - if not too busy and still looks good
Should not have
• - Look busy
- Reverse Logo
- Not follow the Brand Guide
- Anything in the background but one solid color from the brief

```html
<!DOCTYPE html>
<html lang="en">
<head>
<meta charset="utf-8">
<title>Tidy Belly Talks – Podcast Cover</title>
<link rel="stylesheet" href="https://fonts.googleapis.com/css2?family=Oswald:wght@400;500;700&display=swap">
<style>
  :root {
    --navy: #1f3f73;
    --pink: #d93a84;
    --paper: #ffffff;
    --backdrop: #c9c9c9;
    --photo-light: #f1f2f4;
    --photo-dark: #dfe2e7;
  }
  html, body {
    margin: 0;
    width: 693px;
    height: 1200px;
    overflow: hidden;
    background: var(--backdrop);
  }
  .podcast-cover {
    position: absolute;
    left: 36px;
    top: 290px;
    width: 620px;
    height: 620px;
  }
  .podcast-cover svg {
    display: block;
    width: 620px;
    height: 620px;
  }
  .cover-text { font-family: "Oswald", sans-serif; }
  .weight-bold { font-weight: 700; }
  .weight-medium { font-weight: 500; }
  .fill-navy { fill: var(--navy); }
  .fill-pink { fill: var(--pink); }
  .show-url { letter-spacing: 6px; }
</style>
</head>
<body>
  <div class="podcast-cover">
    <svg viewBox="0 0 620 620" xmlns="http://www.w3.org/2000/svg">
      <defs>
        <linearGradient id="photo-tone" x1="0" y1="0" x2="0" y2="1">
          <stop offset="0" stop-color="var(--photo-dark)"/>
          <stop offset="1" stop-color="var(--photo-light)"/>
        </linearGradient>
      </defs>

      <rect class="cover-base" x="0" y="0" width="620" height="620" fill="var(--paper)"/>

      <path class="host-photo" role="img" aria-label="Headshot of host Marcus Lindqvar in a white shirt"
            d="M14 608 L14 210 Q14 178 46 178 L330 178 Q362 178 362 210 L362 608 Z"
            fill="url(#photo-tone)"/>

      <rect class="frame-outer" x="2.5" y="2.5" width="615" height="615" fill="none" stroke="var(--navy)" stroke-width="5"/>
      <rect class="frame-inner" x="10" y="10" width="600" height="600" fill="none" stroke="var(--pink)" stroke-width="3"/>

      <g class="brand-name cover-text weight-bold fill-navy">
        <text x="74" y="72" font-size="34" text-anchor="middle">TIDY</text>
        <text x="74" y="116" font-size="34" text-anchor="middle">BELLY</text>
        <text x="74" y="160" font-size="34" text-anchor="middle">TALKS</text>
      </g>

      <text class="headline-lead cover-text weight-medium fill-navy" x="137" y="81" font-size="62" textLength="350" lengthAdjust="spacingAndGlyphs">RISING WITH</text>

      <g class="headline-condition cover-text weight-bold">
        <text class="fill-navy" x="140" y="198" font-size="130" textLength="459" lengthAdjust="spacingAndGlyphs">BRAMWELL'S</text>
        <text class="fill-pink" x="137" y="195" font-size="130" textLength="459" lengthAdjust="spacingAndGlyphs">BRAMWELL'S</text>
        <text class="fill-navy" x="599" y="309" font-size="130" text-anchor="end" textLength="366" lengthAdjust="spacingAndGlyphs">ACHE</text>
        <text class="fill-pink" x="596" y="306" font-size="130" text-anchor="end" textLength="366" lengthAdjust="spacingAndGlyphs">ACHE</text>
      </g>

      <text class="headline-with cover-text weight-medium fill-navy" x="272" y="359" font-size="50" textLength="94" lengthAdjust="spacingAndGlyphs">WITH</text>

      <g class="host-name cover-text weight-bold">
        <text class="fill-pink" x="379" y="424" font-size="122" textLength="220" lengthAdjust="spacingAndGlyphs">MARCUS</text>
        <text class="fill-navy" x="376" y="421" font-size="122" textLength="220" lengthAdjust="spacingAndGlyphs">MARCUS</text>
        <text class="fill-navy" x="376" y="471" font-size="42" textLength="220" lengthAdjust="spacingAndGlyphs">LINDQVAR</text>
      </g>

      <rect class="restroom-figures" role="img" aria-label="Small pair of restroom figures in navy and pink"
            x="474" y="484" width="44" height="40" rx="4" fill="var(--navy)" opacity="0.85"/>

      <text class="show-url cover-text weight-medium fill-pink" x="596" y="586" font-size="17" text-anchor="end">WWW.TIDYBELLYTALKS.NET</text>
    </svg>
  </div>
</body>
</html>
```